Autism Awareness Card

Want to have an April is Autism Awareness Month card made like the attached sign...with the red, white and blue and early signs along with our contact info...Mara Dunholt 305.618.2039 email: harborlightsupportnet@mailvento.com and website: harborlightsupportnet.com and find us on Facebook: HLS - Harborlight Support Network
and more signs if they will fit
upset by change in routine, sensory issues , lacks smiling , gastrointestinal disorders, spins objects or self, inappropriate laughing, does not point or gesture
I want it to have a puzzle piece and be something like the attached but the number is now its 1 in 68
2 sided - color
can use a heart that says "I love someone with autism" if it fits also
can use a picture of boy or not - whatever looks best

```html
<!DOCTYPE html>
<html lang="en">
<head>
<meta charset="utf-8">
<title>Harborlight Support Network – Autism Awareness Card</title>
<link rel="stylesheet" href="https://fonts.googleapis.com/css2?family=Anton&family=Oswald:wght@500;600;700&family=Roboto+Condensed:wght@400;700&family=Montserrat:wght@800&family=Lobster&display=swap">
<style>
  :root{
    --red:#e2000f;
    --black:#1c1c1c;
    --white:#ffffff;
    --blue-deep:#0b3f8f;
    --blue-bright:#14a6e3;
  }
  *{margin:0;padding:0;box-sizing:border-box;}
  html,body{width:845px;height:1200px;overflow:hidden;}
  body{
    position:relative;
    background:linear-gradient(180deg,var(--blue-deep) 0%,#1673c9 30%,var(--blue-bright) 55%,#1673c9 78%,var(--blue-deep) 100%);
    font-family:"Roboto Condensed",sans-serif;
  }
  .card{position:absolute;width:700px;height:537px;box-shadow:6px 8px 14px rgba(0,0,0,.45);overflow:hidden;}

  /* ---------- front ---------- */
  .card--front{left:70px;top:32px;background:var(--white);}
  .front__header{position:absolute;left:0;top:0;width:100%;height:76px;background:var(--red);border-bottom:6px solid var(--black);
    display:flex;align-items:center;justify-content:center;}
  .front__title{font-family:"Anton",sans-serif;font-size:44px;color:var(--white);letter-spacing:.3px;white-space:nowrap;}
  .heart-art{position:absolute;left:32px;top:112px;width:304px;height:264px;border-radius:120px 120px 150px 150px;
    background:linear-gradient(135deg,#e2182b 0%,#f7d51d 35%,#37b3e8 60%,#5cb94a 85%);
    display:flex;align-items:center;justify-content:center;}
  .heart-art__text{font-family:"Lobster",cursive;font-size:25px;line-height:1.2;color:var(--white);text-align:center;
    transform:rotate(-4deg);margin-top:-40px;}
  .stat{position:absolute;left:336px;top:108px;width:350px;text-align:center;}
  .stat__number{font-family:"Anton",sans-serif;font-size:136px;line-height:1;color:var(--red);white-space:nowrap;letter-spacing:2px;}
  .stat__line{font-family:"Oswald",sans-serif;font-weight:700;font-size:31px;line-height:1;color:var(--black);white-space:nowrap;margin-top:6px;transform:scaleX(.92);}
  .stat__word{font-family:"Anton",sans-serif;font-size:118px;line-height:1;color:var(--red);white-space:nowrap;letter-spacing:1px;margin-top:2px;}
  .front__footer{position:absolute;left:0;top:418px;width:100%;height:119px;background:var(--red);border-top:8px solid var(--black);}
  .help-tab{position:absolute;left:0;top:400px;height:32px;width:156px;background:var(--black);
    clip-path:polygon(0 0,88% 0,100% 100%,0 100%);
    font-family:"Oswald",sans-serif;font-weight:700;font-size:23px;line-height:32px;color:var(--white);padding-left:24px;}
  .contact{position:absolute;left:24px;top:432px;color:var(--white);}
  .contact__name{font-family:"Oswald",sans-serif;font-weight:600;font-size:23px;line-height:30px;}
  .contact__row{display:flex;align-items:center;font-size:18px;height:27px;white-space:nowrap;}
  .contact__item{display:flex;align-items:center;gap:8px;margin-right:26px;}
  .contact__item--small{font-size:15px;gap:6px;margin-right:0;}
  .contact__icon{width:17px;height:17px;flex:none;}
  .social-square{width:17px;height:17px;background:var(--white);border-radius:2px;flex:none;}

  /* ---------- back ---------- */
  .card--back{left:114px;top:602px;background:var(--red);}
  .stripe{position:absolute;left:0;width:314px;height:14px;background:var(--white);}
  .stripe--one{top:28px;}
  .stripe--two{top:56px;width:308px;}
  .flags-tab{position:absolute;left:310px;top:28px;width:390px;height:42px;background:var(--black);
    clip-path:polygon(10px 0,100% 0,100% 100%,0 100%);
    font-family:"Montserrat",sans-serif;font-weight:800;font-size:29px;line-height:42px;color:var(--white);padding-left:20px;letter-spacing:.5px;}
  .photo-frame{position:absolute;left:40px;top:96px;width:232px;height:310px;background:var(--black);transform:rotate(-2deg);}
  .photo{position:absolute;left:52px;top:90px;width:220px;height:302px;
    background:linear-gradient(180deg,#2a4aa6 0%,#3a5cb5 45%,#c79a78 70%,#1e2b4e 100%);}
  .slogan{position:absolute;left:0;top:406px;width:326px;text-align:center;font-family:"Lobster",cursive;font-size:27px;color:var(--white);}
  .hope-box{position:absolute;left:0;top:450px;width:326px;height:87px;background:var(--black);
    clip-path:polygon(0 0,96% 0,100% 100%,0 100%);text-align:center;color:var(--white);font-family:"Oswald",sans-serif;font-weight:700;padding-top:6px;}
  .hope-box__line{font-size:22px;line-height:30px;letter-spacing:-.3px;}
  .hope-box__big{font-size:32px;line-height:40px;}
  .flags{position:absolute;left:336px;top:86px;list-style:none;}
  .flags__item{display:flex;align-items:center;height:40px;font-family:"Oswald",sans-serif;font-weight:500;font-size:24px;color:var(--white);white-space:nowrap;}
  .flags__tick{width:26px;height:26px;margin-right:12px;flex:none;}
</style>
</head>
<body>
<svg width="0" height="0" style="position:absolute">
  <defs>
    <symbol id="tick-box" viewBox="0 0 26 26">
      <rect x="2" y="4" width="20" height="20" fill="none" stroke="#fff" stroke-width="2.6"/>
      <path d="M6 13 L11 19 L24 2" fill="none" stroke="#fff" stroke-width="3.4" stroke-linecap="round" stroke-linejoin="round"/>
    </symbol>
  </defs>
</svg>

<section class="card card--front">
  <header class="front__header"><h1 class="front__title">Harborlight Support Network.com</h1></header>
  <div class="heart-art" role="img" aria-label="Heart made of colourful puzzle pieces">
    <p class="heart-art__text">I Love Someone<br>with Autism</p>
  </div>
  <div class="stat">
    <p class="stat__number">1 in 68</p>
    <p class="stat__line">WILL BE DIAGNOSED WITH</p>
    <p class="stat__word">AUTISM</p>
  </div>
  <div class="front__footer"></div>
  <div class="help-tab">WE CA HELP</div>
  <div class="contact">
    <p class="contact__name">MARA DUNHOLT</p>
    <div class="contact__row">
      <span class="contact__item">
        <svg class="contact__icon" viewBox="0 0 18 18"><circle cx="9" cy="9" r="9" fill="#fff"/><rect x="6" y="4" width="6" height="10" rx="1" fill="#e2000f"/></svg>
        305.618.2039
      </span>
      <span class="contact__item">
        <svg class="contact__icon" viewBox="0 0 18 18"><circle cx="9" cy="9" r="8" fill="none" stroke="#fff" stroke-width="1.6"/><rect x="4.5" y="6" width="9" height="6.5" fill="none" stroke="#fff" stroke-width="1.4"/><path d="M4.5 6 L9 10 L13.5 6" fill="none" stroke="#fff" stroke-width="1.4"/></svg>
        harborlightsupportnet@mailvento.com
      </span>
    </div>
    <div class="contact__row">
      <span class="contact__item">
        <svg class="contact__icon" viewBox="0 0 18 18" fill="none" stroke="#fff" stroke-width="1.5"><circle cx="9" cy="9" r="8"/><ellipse cx="9" cy="9" rx="3.5" ry="8"/><path d="M1 9h16M2.5 5h13M2.5 13h13"/></svg>
        www.harborlightsupportnet.com
      </span>
      <span class="contact__item contact__item--small">
        <span class="social-square"></span>
        HLS-Harborlight Support Network
      </span>
    </div>
  </div>
</section>

<section class="card card--back">
  <div class="stripe stripe--one"></div>
  <div class="stripe stripe--two"></div>
  <h2 class="flags-tab">RED FLAGS</h2>
  <div class="photo-frame"></div>
  <div class="photo" role="img" aria-label="School portrait of a smiling boy"></div>
  <p class="slogan">Early Intervention is Key</p>
  <div class="hope-box">
    <p class="hope-box__line">THERE IS HOPE - 305-618-2039</p>
    <p class="hope-box__big">RECOVERY IS POSSIBLE</p>
  </div>
  <ul class="flags">
    <li class="flags__item"><svg class="flags__tick"><use href="#tick-box"/></svg>Upset by change in routine</li>
    <li class="flags__item"><svg class="flags__tick"><use href="#tick-box"/></svg>Sensory issues</li>
    <li class="flags__item"><svg class="flags__tick"><use href="#tick-box"/></svg>Lacks smiling</li>
    <li class="flags__item"><svg class="flags__tick"><use href="#tick-box"/></svg>Gastrointestinal disorders</li>
    <li class="flags__item"><svg class="flags__tick"><use href="#tick-box"/></svg>Spins objects or self</li>
    <li class="flags__item"><svg class="flags__tick"><use href="#tick-box"/></svg>Inappropriate laughing</li>
    <li class="flags__item"><svg class="flags__tick"><use href="#tick-box"/></svg>Does not point or gesture</li>
    <li class="flags__item"><svg class="flags__tick"><use href="#tick-box"/></svg>Repetative Behaviors</li>
    <li class="flags__item"><svg class="flags__tick"><use href="#tick-box"/></svg>Avoids Eye Contact</li>
    <li class="flags__item"><svg class="flags__tick"><use href="#tick-box"/></svg>Hand Flapping</li>
    <li class="flags__item"><svg class="flags__tick"><use href="#tick-box"/></svg>Language Delay</li>
  </ul>
</section>
</body>
</html>
```